Lantern Vigor
Basketball Fitness Training
Lantern Vigor -
Creative Brief
Modern
Doran Fisk
Health and Fitness Coach
tavmirlo@quillpost.example
www.lanternvigor.example
Youth Development Clinics Private 1 on 1 Sessions Executive Training Women's Fitness Cross Training

```html
<!DOCTYPE html>
<html lang="en">
<head>
<meta charset="utf-8">
<title>Lantern Vigor Stationery</title>
<link href="https://fonts.googleapis.com/css2?family=Archivo:wght@400;700;800&display=swap" rel="stylesheet">
<style>
:root{
  --board:#2f2f31;
  --board-dark:#262628;
  --navy:#1b2d86;
  --orange:#e2561c;
  --accent:#d8322a;
  --paper:#ffffff;
  --paper-shade:#eceef2;
  --caption:#9a9a9c;
  --ink:#2a2a2a;
}
*{margin:0;padding:0;box-sizing:border-box}
html,body{width:1200px;height:365px;overflow:hidden}
body{background:radial-gradient(circle at 50% 40%,var(--board) 0%,var(--board-dark) 100%);font-family:'Archivo',sans-serif;position:relative}
.abs{position:absolute}
.brand{display:flex;align-items:center;gap:6px}
.brand-dot{border-radius:50%;background:var(--orange);flex:none}
.brand-name{font-weight:800;white-space:nowrap}
.tagline{color:var(--accent);font-weight:700}
.caption{color:var(--caption);font-size:6px;text-align:center}

.hero{left:30px;top:12px}
.hero .brand-name{color:#fff;font-size:30px}
.hero .brand-dot{width:26px;height:26px}
.hero .tagline{font-size:13px;margin-left:32px;margin-top:1px}
.section-title{left:250px;top:128px;color:#bdbdbf;font-size:8px}

.card{width:100px;height:56px;border-radius:3px;padding:6px;font-size:4.5px;line-height:1.45}
.card-front{background:var(--paper);color:var(--ink)}
.card-back{background:var(--navy);color:#fff}
.card .person{font-weight:700;font-size:6px}
.card .brand-name{font-size:7.5px;color:var(--navy)}
.card .brand-dot{width:8px;height:8px}
.card-back .brand-name{color:#fff}
.card .rule{height:2px;background:var(--orange);margin:3px 0}

.letterhead{left:331px;top:19px;width:166px;height:322px;background:var(--paper)}
.letterhead .brand{position:absolute;left:8px;top:8px}
.letterhead .brand-name{font-size:10px;color:var(--navy)}
.letterhead .brand-dot{width:10px;height:10px}
.letterhead .contact{position:absolute;right:8px;top:8px;font-size:4px;color:#666;text-align:right;line-height:1.5}
.letterhead .band{position:absolute;left:0;right:0;bottom:0;height:5px;background:var(--navy)}

.envelope{left:576px;top:216px;width:228px;height:84px;background:var(--paper)}
.envelope .brand{position:absolute;left:10px;top:10px}
.envelope .brand-name{font-size:11px;color:var(--navy)}
.envelope .brand-dot{width:11px;height:11px}
.envelope .tagline{position:absolute;left:27px;top:25px;font-size:5.5px}
.envelope .band{position:absolute;left:0;right:0;bottom:0;height:10px;background:var(--navy)}

.env-back{width:240px;height:62px}
.seal{position:absolute;left:50%;top:38%;width:14px;height:14px;margin-left:-7px;border-radius:50%;background:var(--orange);border:1.5px solid #fff}
</style>
</head>
<body>

<div class="abs hero">
  <div class="brand"><span class="brand-dot"></span><span class="brand-name">Lantern Vigor</span></div>
  <div class="tagline">Basketball Fitness Training</div>
</div>
<div class="abs section-title">Business Cards</div>

<!-- business cards -->
<div class="abs card card-front" style="left:22px;top:149px">
  <div class="person">Doran Fisk</div>
  <div>Health and Fitness Coach</div>
  <div class="rule"></div>
  <div>tavmirlo@quillpost.example</div>
  <div>www.lanternvigor.example</div>
</div>
<div class="abs card card-back" style="left:132px;top:149px">
  <div class="person">Doran Fisk</div>
  <div>Health and Fitness Coach</div>
  <div class="rule"></div>
  <div>tavmirlo@quillpost.example</div>
  <div>www.lanternvigor.example</div>
</div>
<div class="abs caption" style="left:22px;top:209px;width:100px">Front Card Style One</div>
<div class="abs caption" style="left:132px;top:209px;width:100px">Back Card Style One</div>

<div class="abs card card-front" style="left:22px;top:242px">
  <div>Youth Development Clinics</div>
  <div>Private 1 on 1 Sessions</div>
  <div>Executive Training</div>
  <div>Women's Fitness</div>
  <div>Cross Training</div>
</div>
<div class="abs card card-back" style="left:132px;top:242px">
  <div class="brand" style="margin-top:14px"><span class="brand-dot"></span><span class="brand-name">Lantern Vigor</span></div>
</div>
<div class="abs caption" style="left:22px;top:302px;width:100px">Front Card Style Two</div>
<div class="abs caption" style="left:132px;top:302px;width:100px">Back Card Style Two</div>

<!-- letterhead -->
<div class="abs letterhead">
  <div class="brand"><span class="brand-dot"></span><span class="brand-name">Lantern Vigor</span></div>
  <div class="contact">tavmirlo@quillpost.example<br>www.lanternvigor.example</div>
  <div class="band"></div>
</div>
<div class="abs caption" style="left:331px;top:345px;width:166px">Letterhead Design</div>

<!-- business envelope -->
<div class="abs envelope">
  <div class="brand"><span class="brand-dot"></span><span class="brand-name">Lantern Vigor</span></div>
  <div class="tagline">Basketball Fitness Training</div>
  <div class="band"></div>
</div>
<div class="abs caption" style="left:576px;top:305px;width:228px">Envelope Front Design</div>

<!-- envelope backs -->
<div class="abs env-back" style="left:888px;top:48px">
  <svg width="240" height="62" viewBox="0 0 240 62"><rect width="240" height="62" fill="var(--orange)"/><path d="M0 0 L120 34 L240 0" fill="none" stroke="#c44814" stroke-width="1"/></svg>
  <span class="seal" style="background:var(--navy)"></span>
</div>
<div class="abs env-back" style="left:888px;top:100px">
  <svg width="240" height="62" viewBox="0 0 240 62"><rect width="240" height="62" fill="var(--navy)"/><path d="M0 0 L120 34 L240 0" fill="none" stroke="#13226a" stroke-width="1"/></svg>
  <span class="seal"></span>
</div>
<div class="abs env-back" style="left:888px;top:152px;height:64px">
  <svg width="240" height="64" viewBox="0 0 240 64"><rect width="240" height="64" fill="var(--paper)"/><path d="M0 0 L120 36 L240 0" fill="none" stroke="var(--paper-shade)" stroke-width="1.5"/></svg>
  <span class="seal"></span>
</div>
<div class="abs caption" style="left:888px;top:222px;width:240px">Envelope Back Design</div>

</body>
</html>
```